Online Art Gallery & Art Management Firm looking for a business card

I'm launching an online art gallery (paintings, photography, drawings, furniture, books, ...) where people can buy all types of art. It's a platform where young and unknown artists can showcase their oeuvre.

Additionally, the venture will act as my advising company for artists. I help them out with their business side of life and become their representative.

The company name: The Velmora House
Logo is attached

I'm looking for something very classy and upmarket.
Updates

Reason: Logo wasn't finished yet...

The design should include the following information: - Name: Pieter Drovensky - Title: Founder - Mobile: +32 (0) 485 613 204 - E-mail: pieter@velmora-house.net - Website www.velmora-house.net I prefer the have the logo (without website) on the one side and the information on the other. Best regards Pieter

Target Market(s)

Art buyers / art dealers / artists / middle class / upmarket /

Industry/Entity Type

Artists

Colors

Designer to choose colors to be used in the design.

Requirements
Must have
• Must communicate credibility, trust and integrity
Nice to have
• Something classy, chique
Should not have
• Nothing to artistic or creative

```html
<!DOCTYPE html>
<html lang="en">
<head>
<meta charset="utf-8">
<title>The Velmora House — Business Card</title>
<link rel="stylesheet" href="https://fonts.googleapis.com/css2?family=PT+Serif:wght@400&display=swap">
<style>
  :root {
    --page-bg: #e9e6e1;
    --card-black: #0b0b0c;
    --card-edge: #1c1c1e;
    --ink-light: #f2f2f2;
    --ink-soft: #cfcfcf;
    --rule: #5a5a5c;
  }
  * { margin: 0; padding: 0; box-sizing: border-box; }
  html, body {
    width: 1200px;
    height: 954px;
    overflow: hidden;
    background: var(--page-bg);
  }
  .sheet {
    width: 1200px;
    height: 954px;
    display: flex;
    flex-direction: column;
    align-items: center;
    justify-content: center;
    gap: 40px;
  }
  .card {
    position: relative;
    width: 640px;
    height: 414px;
    background: var(--card-black);
    border: 1px solid var(--card-edge);
    box-shadow: 0 6px 18px rgba(0,0,0,0.25);
    overflow: hidden;
    color: var(--ink-light);
    font-family: "PT Serif", serif;
  }
  .company-name {
    font-family: "PT Serif", serif;
    font-weight: 400;
    color: var(--ink-light);
    white-space: nowrap;
  }

  /* Details side */
  .card-front .company-name {
    position: absolute;
    left: 46px;
    top: 160px;
    font-size: 34px;
    line-height: 1;
  }
  .card-front .divider {
    position: absolute;
    left: 0;
    right: 0;
    top: 214px;
    height: 1px;
    background: var(--rule);
  }
  .holder {
    position: absolute;
    right: 44px;
    top: 42px;
    text-align: right;
  }
  .holder-name {
    font-size: 22px;
    color: var(--ink-light);
  }
  .holder-title {
    margin-top: 6px;
    font-size: 17px;
    color: var(--ink-soft);
  }
  .contact-list {
    position: absolute;
    left: 46px;
    bottom: 40px;
    list-style: none;
    font-size: 16px;
    color: var(--ink-light);
  }
  .contact-list li {
    display: flex;
    align-items: center;
    gap: 14px;
    height: 30px;
  }
  .contact-list svg {
    width: 18px;
    height: 18px;
    fill: var(--ink-soft);
    flex: none;
  }

  /* Brand side */
  .card-back {
    display: flex;
    align-items: center;
    justify-content: center;
  }
  .card-back .company-name {
    font-size: 40px;
  }
</style>
</head>
<body>
<main class="sheet">
  <section class="card card-front" aria-label="Business card, details side">
    <div class="holder">
      <p class="holder-name">Pieter Drovensky</p>
      <p class="holder-title">Founder</p>
    </div>
    <p class="company-name">The Velmora House</p>
    <div class="divider"></div>
    <ul class="contact-list">
      <li>
        <svg viewBox="0 0 24 24" aria-hidden="true"><path d="M6.6 10.8a15.1 15.1 0 0 0 6.6 6.6l2.2-2.2c.3-.3.7-.4 1-.2 1.1.4 2.3.6 3.6.6.6 0 1 .4 1 1V20c0 .6-.4 1-1 1A17 17 0 0 1 3 4c0-.6.4-1 1-1h3.5c.6 0 1 .4 1 1 0 1.3.2 2.5.6 3.6.1.3 0 .7-.2 1z"/></svg>
        <span>+32 (0) 485 613 204</span>
      </li>
      <li>
        <svg viewBox="0 0 24 24" aria-hidden="true"><path d="M3 5h18v14H3zm2 2v.4l7 4.6 7-4.6V7zm0 2.8V17h14V9.8l-7 4.6z"/></svg>
        <span>pieter@velmora-house.net</span>
      </li>
      <li>
        <svg viewBox="0 0 24 24" aria-hidden="true"><path d="M12 2a10 10 0 1 0 0 20 10 10 0 0 0 0-20zm6.9 6h-2.9a15 15 0 0 0-1.3-3.6A8 8 0 0 1 18.9 8zM12 4c.8 1.2 1.5 2.5 1.9 4h-3.8c.4-1.5 1.100-2.8 1.9-4zM4.3 14a8 8 0 0 1 0-4h3.4a16 16 0 0 0 0 4zm.8 2h2.9c.3 1.3.8 2.5 1.3 3.6A8 8 0 0 1 5.1 16zM8 8H5.1a8 8 0 0 1 4.2-3.6C8.8 5.5 8.3 6.7 8 8zm4 12c-.8-1.2-1.500-2.5-1.9-4h3.8c-.4 1.5-1.1 2.8-1.9 4zm2.3-6H9.7a14 14 0 0 1 0-4h4.6a14 14 0 0 1 0 4zm.4 5.6c.5-1.1 1-2.3 1.3-3.6h2.9a8 8 0 0 1-4.2 3.6zM16.3 14a16 16 0 0 0 0-4h3.4a8 8 0 0 1 0 4z"/></svg>
        <span>www.velmora-house.net</span>
      </li>
    </ul>
  </section>

  <section class="card card-back" aria-label="Business card, brand side">
    <p class="company-name">The Velmora House</p>
  </section>
</main>
</body>
</html>
```